Stationary for an International Church

We need a design for various stationery items - letters/envelopes, Word/PowerPoint pages, based on
- the LHF Logo
- the primary color "bright turquoise" ("vivid cyan"), hex #08e8de
- the font family: Frutiger 55 Roman
To get an image of our organization, please visit lanternhill.org, recent blog entries at https://www.lanternhill.org/blog or annual reports at Downloads

Target Market(s)

Congregation and business partners of the Chruch

Font styles to use
Other font styles liked:
• requirement: Frutiger 55 Roman

Colors
33b8a4

Requirements
Must have
• simple, modern design, a bit unique

```html
<!DOCTYPE html>
<html lang="en">
<head>
<meta charset="utf-8">
<title>Lantern Hill Fellowship — Stationery</title>
<link href="https://fonts.googleapis.com/css2?family=Open+Sans:wght@300;400;600;700&display=swap" rel="stylesheet">
<style>
  :root {
    --teal: #4db8bb;
    --swoosh: #c9c9c9;
    --ink: #2b2b2b;
    --body: #6a6a6a;
    --stage: #e4e6e6;
    --paper-top: #ffffff;
    --paper-bottom: #e7e7e7;
  }
  * { margin: 0; padding: 0; box-sizing: border-box; }
  html, body { width: 1200px; height: 974px; overflow: hidden; }
  body {
    background: var(--stage);
    font-family: "Open Sans", Arial, sans-serif;
    position: relative;
  }
  .sheet {
    position: absolute;
    background: linear-gradient(to bottom, var(--paper-top) 25%, var(--paper-bottom) 100%);
    box-shadow: 0 2px 8px rgba(0,0,0,0.12);
    overflow: hidden;
  }
  .letterhead { left: 40px; top: 91px; width: 560px; height: 792px; }
  .envelope   { left: 640px; top: 560px; width: 520px; height: 216px; }

  .brand { position: absolute; text-align: center; color: var(--teal); }
  .brand-name { font-weight: 600; white-space: nowrap; }
  .brand-rule { height: 1px; background: var(--teal); margin: 4px 0 5px; }
  .brand-tagline { letter-spacing: 0.6px; white-space: nowrap; }

  .address { position: absolute; color: var(--ink); font-style: normal; white-space: nowrap; }
  .divider { position: absolute; width: 1px; background: var(--teal); }
  .contacts { position: absolute; color: var(--ink); list-style: none; }
  .contacts li { display: flex; align-items: center; white-space: nowrap; }
  .contacts svg { fill: var(--teal); flex: none; }

  .footer-wave { position: absolute; left: 0; bottom: 0; width: 100%; }
  .web { position: absolute; color: #fff; letter-spacing: 0.8px; }
  .web b { font-weight: 600; }

  /* letterhead */
  .letterhead .brand { left: 24px; top: 92px; width: 112px; }
  .letterhead .brand-name { font-size: 6.4px; letter-spacing: 0.6px; }
  .letterhead .brand-tagline { font-size: 6.2px; }
  .letterhead .address { left: 289px; top: 50px; font-size: 10px; line-height: 14.2px; }
  .letterhead .divider { left: 386px; top: 55px; height: 36px; }
  .letterhead .contacts { left: 408px; top: 50px; font-size: 10px; line-height: 14.2px; }
  .letterhead .contacts svg { width: 9px; height: 9px; margin-right: 8px; }
  .letterhead .footer-wave { height: 50px; }
  .letterhead .web { right: 30px; bottom: 10px; font-size: 11px; }

  .salutation {
    position: absolute; left: 55px; top: 207px;
    font-size: 13.5px; font-weight: 600; color: var(--teal);
  }
  .date {
    position: absolute; right: 55px; top: 210px;
    font-size: 10px; color: var(--body);
  }
  .date b { color: var(--teal); font-weight: 700; }
  .letter-body {
    position: absolute; left: 55px; top: 240px; width: 449px;
    font-size: 10px; font-weight: 300; line-height: 14.1px; color: var(--body);
    text-align: justify; hyphens: auto;
  }
  .letter-body p + p { margin-top: 14.1px; }
  .closing {
    position: absolute; left: 55px; top: 573px;
    font-size: 13.5px; font-weight: 600; color: var(--teal);
  }
  .signature {
    position: absolute; left: 55px; top: 598px; width: 115px; height: 28px;
    background: linear-gradient(90deg, #ececec, #f4f4f4);
  }

  /* envelope */
  .envelope .brand { left: 20px; top: 74px; width: 80px; }
  .envelope .brand-name { font-size: 5.2px; letter-spacing: 0.5px; }
  .envelope .brand-rule { margin: 3px 0 4px; }
  .envelope .brand-tagline { font-size: 4.6px; }
  .envelope .address { left: 302px; top: 42px; font-size: 8px; line-height: 11px; }
  .envelope .divider { left: 383px; top: 45px; height: 28px; }
  .envelope .contacts { left: 401px; top: 42px; font-size: 8px; line-height: 11px; }
  .envelope .contacts svg { width: 7px; height: 7px; margin-right: 6px; }
  .envelope .footer-wave { height: 38px; }
  .envelope .web { right: 23px; bottom: 8px; font-size: 8.6px; }
</style>
</head>
<body>

<section class="sheet letterhead" aria-label="Letterhead">
  <div class="brand">
    <div class="brand-name">LANTERN HILL FELLOWSHIP</div>
    <div class="brand-rule"></div>
    <div class="brand-tagline">God’s house, my home</div>
  </div>

  <address class="address">
    4-2-9 Kasumidai,<br>Nishiyama-ku<br>Tokyo, 160-0042
  </address>
  <div class="divider"></div>
  <ul class="contacts">
    <li><svg viewBox="0 0 10 10"><path d="M2 0.5 L3.6 2.6 L2.8 3.8 Q3.8 5.8 6.2 7.2 L7.4 6.4 L9.5 8 L8.4 9.6 Q4.5 9.4 1.8 6 Q0.4 3.8 0.6 1.6 Z"/></svg>(03) 5550-0147</li>
    <li><svg viewBox="0 0 10 10"><rect x="2.5" y="0.5" width="5" height="2.5"/><rect x="0.5" y="3.5" width="9" height="4" rx="0.8"/><rect x="2.5" y="6.5" width="5" height="3"/></svg>(03) 5550-1942</li>
    <li><svg viewBox="0 0 10 10"><path d="M0.5 2 H9.5 V8.5 H0.5 Z M0.5 2 L5 5.6 L9.5 2"/></svg>info@lanternhill.org</li>
  </ul>

  <div class="salutation">Dear Martin,</div>
  <div class="date"><b>Date:</b> 00.00.0000</div>

  <div class="letter-body">
    <p>Lorem ipsum dolor sit amet, consectetur adipiscing elit, sed do eiusmod tempor incididunt ut labore et dolore magna aliqua. Ut enim ad minim veniam, quis nostrud exercitation ullamco laboris nisi ut aliquip ex ea commodo consequat. Duis aute irure dolor in reprehenderit in voluptate velit esse cillum dolore eu fugiat nulla pariatur. Excepteur sint occaecat cupidatat non proident, sunt in culpa qui officia deserunt mollit anim id est Proident, sunt in culpa qui xcepteur sint occaecat cupidatat officia laborum. onsectetur adipiscing elit, sed do eiusmod .</p>
    <p>Lorem ipsum dolor sit amet, consectetur adipiscing elit, sed do eiusmod tempor incididunt ut labore et dolore magna aliqua. Ut enim ad minim veniam, quis nostrud exercitation ullamco laboris nisi ut aliquip ex ea commodo consequat. Duis aute irure dolor in reprehenderit in vo orem ipsum dolor sit amet, consectetur adipiscing elit, sed do eiusmod tempor incididunt ut labore et dolore magna aliqua. Ut enim ad minim veniam, quis nostrud exercitation ullamco laboris nisi ut aliquip ex ea commodo consequat. Duis aute irure dolor in reprehenderit in voluptate velit esse cillum dolore eu fugiat nulla pariatur. Excepteur sint occaecat cupidatat non proident, sunt in culpa qui officia deserunt mollit anim id est Proident, sunt in culpa qui xcepteur sint occaecat cupidatat officia laborum. onsectetur adipiscing elit, sed do eiusmod .</p>
    <p>Lorem ipsum dolor sit amet, consectetur adipiscing elit, sed do eiusmod tempor incididunt ut labore et dolore magna aliqua. Ut enim ad minim veniam, quis nostrud exercitation ullamco laboris nisi ut aliquip ex ea commodo consequat. Duis aute irure dolor in reprehenderit in voluptate velit esse cillum dolore eu fugiat nulla pariatur. Excepteur sint occaecat cupidatat non proident, sunt in culpa qui officia deserunt mollit anim id est Proident, sunt in culpa qui xcepteur sint occaecat cupidatat officia laborum. onsectetur adipiscing elit, sed do eiusmod .</p>
  </div>

  <div class="closing">Sincerely</div>
  <div class="signature" role="img" aria-label="Handwritten signature of the sender"></div>

  <svg class="footer-wave" viewBox="0 0 1000 90" preserveAspectRatio="none" aria-hidden="true">
    <path fill="var(--swoosh)" d="M430 90 C590 30 820 4 1000 2 L1000 6 C840 10 650 40 555 90 Z"/>
    <path fill="var(--teal)" d="M575 90 C690 42 850 20 1000 18 L1000 90 Z"/>
  </svg>
  <div class="web">www.<b>lanternhill</b>.org</div>
</section>

<section class="sheet envelope" aria-label="Envelope">
  <div class="brand">
    <div class="brand-name">LANTERN HILL FELLOWSHIP</div>
    <div class="brand-rule"></div>
    <div class="brand-tagline">God’s house, my home</div>
  </div>

  <address class="address">
    4-2-9 Kasumidai,<br>Nishiyama-ku<br>Tokyo, 160-0042
  </address>
  <div class="divider"></div>
  <ul class="contacts">
    <li><svg viewBox="0 0 10 10"><path d="M2 0.5 L3.6 2.6 L2.8 3.8 Q3.8 5.8 6.2 7.2 L7.4 6.4 L9.5 8 L8.4 9.6 Q4.5 9.4 1.8 6 Q0.4 3.8 0.6 1.6 Z"/></svg>(03) 5550-0147</li>
    <li><svg viewBox="0 0 10 10"><rect x="2.5" y="0.5" width="5" height="2.5"/><rect x="0.5" y="3.5" width="9" height="4" rx="0.8"/><rect x="2.5" y="6.5" width="5" height="3"/></svg>(03) 5550-1942</li>
    <li><svg viewBox="0 0 10 10"><path d="M0.5 2 H9.5 V8.5 H0.5 Z M0.5 2 L5 5.6 L9.5 2"/></svg>info@lanternhill.org</li>
  </ul>

  <svg class="footer-wave" viewBox="0 0 1000 90" preserveAspectRatio="none" aria-hidden="true">
    <path fill="var(--swoosh)" d="M505 90 C650 30 830 2 1000 0 L1000 5 C850 8 690 40 600 90 Z"/>
    <path fill="var(--teal)" d="M620 90 C730 40 870 22 1000 20 L1000 90 Z"/>
  </svg>
  <div class="web">www.<b>lanternhill</b>.org</div>
</section>

</body>
</html>
```